Carpentry company Needs a business card design

We need a design for a Carpentry / building company, business card. Please think of designs out of the ordinary and try to make it eye catching. Our existing logo will need to be incorporated in the design. However feel free to change the colours of the logo to suit your design. I would like to see some designs with green /black and orange incorporated into it.These are not the only colours accepted and all designs that appeal will be accepted.

Please contact me should you have any questions
Thanks Martin

Target Market(s)

General Public seeking carpentry work

Industry/Entity Type

Business

Contact Information for Business Card

- Current company logo ( colours can be changed)
-Phone number ,
- info@brelvanbuild.com.au
- brelvanbuild.com.au
-the facebook symbol

Font styles to use
Other font styles liked:
• You choose

Requirements
Must have
• Services we provide
• - Renovations
• -Deckings & Pergolas
• -Kitchens
• - Bathrooms
• - Intricate details
Nice to have
• an awesome design
Should not have
• Tools on the business card

```html
<!DOCTYPE html>
<html lang="en">
<head>
<meta charset="utf-8">
<title>Brelvan Build — Business Card</title>
<link rel="stylesheet" href="https://fonts.googleapis.com/css2?family=Source+Sans+3:wght@400;600;700&display=swap">
<style>
  :root {
    --backdrop: #3b3431;
    --card: #121212;
    --ink: #f2f2f2;
    --ink-soft: #cfcfcf;
    --accent: #c98b45;
    --rule: #555555;
  }
  * { margin: 0; padding: 0; box-sizing: border-box; }
  html, body {
    width: 1200px; height: 814px; overflow: hidden;
    background: var(--backdrop);
    font-family: "Source Sans 3", sans-serif;
    color: var(--ink);
  }
  .canvas { position: relative; width: 1200px; height: 814px; }
  .card {
    position: absolute; top: 262px;
    width: 520px; height: 298px;
    background: var(--card);
    box-shadow: 0 10px 30px rgba(0,0,0,0.45);
  }
  .card--front { left: 60px; }
  .card--back { left: 620px; }

  /* Front */
  .brand {
    position: absolute; left: 46px; top: 0; height: 100%; width: 210px;
    display: flex; align-items: center; gap: 12px;
  }
  .brand__mark { width: 18px; height: 18px; background: var(--accent); flex: none; }
  .brand__name { font-size: 30px; font-weight: 700; letter-spacing: 0.5px; color: var(--ink); line-height: 1; }
  .divider {
    position: absolute; left: 270px; top: 64px; width: 1px; height: 170px;
    background: var(--rule);
  }
  .contact { position: absolute; left: 290px; top: 72px; }
  .contact__name { font-size: 21px; font-weight: 700; line-height: 1.1; }
  .contact__role { font-size: 15px; color: var(--accent); margin-bottom: 8px; }
  .contact__list { list-style: none; }
  .contact__item {
    display: flex; align-items: center; gap: 9px;
    font-size: 15px; color: var(--ink-soft); line-height: 24px;
  }
  .contact__icon { width: 13px; height: 13px; flex: none; fill: var(--ink); }
  .contact__icon--square { width: 11px; height: 11px; background: var(--ink); margin: 0 1px; }

  /* Back */
  .back-brand {
    position: absolute; left: 0; right: 0; top: 74px;
    display: flex; justify-content: center; align-items: center; gap: 12px;
  }
  .back-brand .brand__mark { width: 22px; height: 22px; }
  .back-brand .brand__name { font-size: 34px; }
  .services {
    position: absolute; left: 0; right: 0; top: 176px;
    text-align: center; font-size: 15px; color: var(--ink-soft); line-height: 24px;
  }
  .services__dot {
    display: inline-block; width: 6px; height: 6px; border-radius: 50%;
    background: var(--accent); margin: 0 6px; vertical-align: middle;
  }
</style>
</head>
<body>
<main class="canvas">
  <section class="card card--front" aria-label="Business card front">
    <div class="brand">
      <span class="brand__mark"></span>
      <span class="brand__name">BRELVAN<br>BUILD</span>
    </div>
    <div class="divider"></div>
    <div class="contact">
      <p class="contact__name">Martin</p>
      <p class="contact__role">Owner</p>
      <ul class="contact__list">
        <li class="contact__item">
          <svg class="contact__icon" viewBox="0 0 24 24"><path d="M6.6 10.8a15.1 15.1 0 0 0 6.6 6.6l2.2-2.2a1 1 0 0 1 1-.25 11.4 11.4 0 0 0 3.6.57 1 1 0 0 1 1 1V20a1 1 0 0 1-1 1A17 17 0 0 1 3 4a1 1 0 0 1 1-1h3.5a1 1 0 0 1 1 1c0 1.25.2 2.45.57 3.6a1 1 0 0 1-.25 1z"/></svg>
          612 555 0148
        </li>
        <li class="contact__item"><span class="contact__icon contact__icon--square"></span>brelvanbuild</li>
        <li class="contact__item">
          <svg class="contact__icon" viewBox="0 0 24 24"><path d="M2 5h20v14H2z M3 6l9 7 9-7" fill="none" stroke="#f2f2f2" stroke-width="2"/></svg>
          info@brelvanbuild.com.au
        </li>
        <li class="contact__item">
          <svg class="contact__icon" viewBox="0 0 24 24"><circle cx="12" cy="12" r="9" fill="none" stroke="#f2f2f2" stroke-width="2"/><path d="M3 12h18M12 3c3 3 3 15 0 18M12 3c-3 3-3 15 0 18" fill="none" stroke="#f2f2f2" stroke-width="1.6"/></svg>
          brelvanbuild.com.au
        </li>
      </ul>
    </div>
  </section>

  <section class="card card--back" aria-label="Business card back">
    <div class="back-brand">
      <span class="brand__mark"></span>
      <span class="brand__name">BRELVAN BUILD</span>
    </div>
    <p class="services">
      Renovations<span class="services__dot"></span>Deckings &amp; Pergolas<br>
      Kitchens<span class="services__dot"></span>Bathrooms<span class="services__dot"></span>Intricate details
    </p>
  </section>
</main>
</body>
</html>
```